iOS app design for movie reviews app

I need an app redesign for 5 pages of my iphone app. The app is a social movie reviews app that lets you share and find movies based on friends recommendations. The app is currently live in the app store under the working name tomsDeck, but I will be re-branding under the name "zested". Reviews will now be called "quips". The app is free in the app store and is a good reference for the functionality. Some screenshots can be seen here: https://apps.example-store.com/us/app/tomsdeck/id927461503?mt=8
The 5 pages should have a similar look and feel and do not have to match what is currently live in the app store. I am looking to do an overhaul of the design and am open to completely new designs, this includes color scheme.
1. Splash Screen - page users see when they initially open the app to login. Should include the name of the app (zested) and login with friendhub button, as well as graphics or a logo. Current design should be ignored.
2. Home Page (screenshot #2 on appvault page) - page user sees when they login after their first session. This is where users will normally land and is the primary place users navigate the app. The homepage must have a few elements: searchbar to find movies, user stats (quips, followers, # of time other users have read your quips, # of times other users have viewed your profile page), and six icons to navigate (watchlist, explore, popular, messages, network and my reviews). Watchlist, messages and network icons will have notification messages that come up to show when the user has new activity on those pages. There are currently icons for some of these in the app, but I am open to redesigns of these as well
3. Movie Profile Page - this is a new page to the app where a user can see more detailed information about a specific movie. This page must include poster image, title, genre, release date, rating (PG, R, etc.), length, description, video trailer and actors. A user will get to this page by tapping on the short description on the movie page (screenshot #1 on appvault page) above their friends reviews. This page will not have any reviews, just details about the movie.
4. Explore Page - this is the page where users can perform a specific search for movies. There are two filters that need to be accessible (location of movie and genre). A user can perform a search just for themself and filter by movies they have seen or never seen. They can also search for movies that they want to watch with a friend, so they select a friend and see results that both of them would like.
5. My Reviews Page (screenshot #4 on appvault page)- this page shows all the reviews (quips) that a user has submitted. This is just their number rating as well as the number of views that review has collected from other users. They can be sorted by top rated or most viewed.
Optional: I will also need an app icon that matches the look and feel of the app.
Movie

```html
<!DOCTYPE html>
<html lang="en">
<head>
<meta charset="utf-8">
<title>zested – Splash Screen Page</title>
<link rel="stylesheet" href="https://fonts.googleapis.com/css2?family=Arimo:wght@400;700&family=Source+Sans+3:wght@400&display=swap">
<style>
  :root {
    --page-bg: #ffffff;
    --title-bar: #1e1e1f;
    --title-text: #ffffff;
    --status-bar: #1f3461;
    --status-text: #dfe6f2;
    --orange: #f27a22;
    --orange-deep: #c8552a;
    --orange-light: #f7a11f;
    --orange-edge: #f9a53a;
    --curtain-dark: #5a0a0a;
    --curtain-mid: #8a1414;
    --field-bg: #ffffff;
    --field-border: #222222;
    --cursor: #1a5fd0;
    --white: #ffffff;
  }
  * { box-sizing: border-box; margin: 0; padding: 0; }
  html, body { width: 1200px; height: 1000px; overflow: hidden; background: var(--page-bg); }
  .canvas { position: relative; width: 1200px; height: 1000px; font-family: "Arimo", Arial, sans-serif; }

  .section-bar {
    position: absolute; left: 0; top: 146px; width: 1200px; height: 50px;
    background: var(--title-bar); color: var(--title-text);
    font-family: "Source Sans 3", sans-serif; font-size: 29px;
    display: flex; align-items: center; justify-content: center; padding-left: 2px;
  }

  .screen { position: absolute; top: 358px; width: 320px; height: 480px; overflow: hidden; }
  .screen--splash { left: 237px; }
  .screen--login { left: 663px; }

  .status-bar {
    position: absolute; left: 0; top: 0; width: 100%; height: 20px;
    background: var(--status-bar); color: var(--status-text);
    font-size: 12px; font-weight: 700;
  }
  .status-bar .carrier { position: absolute; left: 5px; top: 3px; }
  .status-bar .wifi { position: absolute; left: 55px; top: 4px; }
  .status-bar .time { position: absolute; left: 0; right: 0; top: 3px; text-align: center; }
  .status-bar .battery { position: absolute; right: 4px; top: 5px; }

  .splash-body {
    position: absolute; left: 0; top: 20px; width: 100%; height: 460px;
    background: linear-gradient(to bottom, var(--orange) 0%, var(--orange) 60%, var(--orange-deep) 100%);
  }
  .splash-name {
    position: absolute; left: 0; right: 0; top: 210px; text-align: center;
    color: var(--white); font-size: 54px; font-weight: 700;
  }

  .app-header {
    position: absolute; left: 0; top: 20px; width: 100%; height: 44px;
    background: linear-gradient(to bottom, #f58a2a, #e2641f);
    color: var(--white); font-size: 26px; font-weight: 700;
    display: flex; align-items: center; justify-content: center;
    border-bottom: 1px solid #6b1a0e;
  }
  .curtain {
    position: absolute; left: 0; top: 64px; width: 100%; height: 416px;
    background: linear-gradient(to right, var(--curtain-dark), var(--curtain-mid) 50%, var(--curtain-dark));
  }

  .login-dialog {
    position: absolute; left: 23px; top: 132px; width: 276px; height: 283px;
    border: 2px solid var(--orange-edge); border-radius: 10px; overflow: hidden;
    background: linear-gradient(to right, var(--orange) 0%, var(--orange) 55%, var(--orange-deep) 100%);
  }
  .login-dialog .shine { position: absolute; left: 0; top: 0; width: 100%; height: 30px; }
  .dialog-title { position: absolute; left: 0; right: 0; top: 50px; text-align: center; color: var(--white); font-size: 17px; font-weight: 700; }
  .field-label { position: absolute; left: 0; right: 0; text-align: center; color: var(--white); font-size: 14px; }
  .field-label--user { top: 78px; }
  .field-label--pass { top: 154px; }
  .field {
    position: absolute; left: 6px; width: 262px; height: 31px;
    background: var(--field-bg); border: 1px solid var(--field-border);
    font-size: 17px; letter-spacing: -1px; color: #000; padding: 3px 0 0 3px;
  }
  .field--user { top: 110px; }
  .field--pass { top: 186px; }
  .field .caret { display: inline-block; width: 3px; height: 22px; background: var(--cursor); vertical-align: middle; margin-left: 4px; }

  .btn {
    position: absolute; top: 227px; width: 127px; height: 42px;
    border: 1px solid #d2661c; border-radius: 4px;
    background: linear-gradient(to bottom, var(--orange-light) 0%, var(--orange-light) 45%, var(--orange) 45%, var(--orange) 100%);
    color: var(--white); font-family: "Arimo", Arial, sans-serif; font-size: 17px; font-weight: 700;
    display: flex; align-items: center; justify-content: center; padding-top: 2px;
  }
  .btn--cancel { left: 6px; }
  .btn--ok { left: 140px; }
</style>
</head>
<body>
<div class="canvas">
  <div class="section-bar">Splash Screen Page</div>

  <section class="screen screen--splash">
    <div class="status-bar">
      <span class="carrier">Carrier</span>
      <svg class="wifi" width="16" height="12" viewBox="0 0 16 12"><path d="M1 4a10 10 0 0 1 14 0M3.5 6.5a6.5 6.5 0 0 1 9 0M6 9a3 3 0 0 1 4 0" fill="none" stroke="#dfe6f2" stroke-width="1.8"/></svg>
      <span class="time">4:06 PM</span>
      <svg class="battery" width="22" height="10" viewBox="0 0 22 10"><rect x="0.5" y="0.5" width="19" height="9" rx="1" fill="none" stroke="#dfe6f2"/><rect x="2" y="2" width="16" height="6" fill="#dfe6f2"/><rect x="20" y="3" width="2" height="4" fill="#dfe6f2"/></svg>
    </div>
    <div class="splash-body">
      <div class="splash-name">zested</div>
    </div>
  </section>

  <section class="screen screen--login">
    <div class="status-bar">
      <span class="carrier">Carrier</span>
      <svg class="wifi" width="16" height="12" viewBox="0 0 16 12"><path d="M1 4a10 10 0 0 1 14 0M3.5 6.5a6.5 6.5 0 0 1 9 0M6 9a3 3 0 0 1 4 0" fill="none" stroke="#dfe6f2" stroke-width="1.8"/></svg>
      <span class="time">4:06 PM</span>
      <svg class="battery" width="22" height="10" viewBox="0 0 22 10"><rect x="0.5" y="0.5" width="19" height="9" rx="1" fill="none" stroke="#dfe6f2"/><rect x="2" y="2" width="16" height="6" fill="#dfe6f2"/><rect x="20" y="3" width="2" height="4" fill="#dfe6f2"/></svg>
    </div>
    <header class="app-header">zested</header>
    <div class="curtain" role="img" aria-label="Red theatre curtain backdrop"></div>

    <div class="login-dialog">
      <svg class="shine" viewBox="0 0 276 30" preserveAspectRatio="none">
        <path d="M0 0H276V14Q138 34 0 14Z" fill="#f48a2e"/>
        <path d="M0 14Q138 34 276 14" fill="none" stroke="#f9b04a" stroke-width="1"/>
      </svg>
      <div class="dialog-title">zested</div>
      <div class="field-label field-label--user">user name</div>
      <div class="field field--user">●●●●●●●●●<span class="caret"></span></div>
      <div class="field-label field-label--pass">password</div>
      <div class="field field--pass">●●●●●●●●●<span class="caret"></span></div>
      <div class="btn btn--cancel">Cancel</div>
      <div class="btn btn--ok">OK</div>
    </div>
  </section>
</div>
</body>
</html>
```